Broschüre für Hüpfburgen, Wasserpark, Zelte....
Zielgruppe
Wir wollen eine Broschüre erstellen. Hüpfburgen, Wasserpark, Zelte.... Vorderseite und Rückseite. Innesseiten sollten wir Bilder und Text austauschen können. A5 Hochformat!!!
Aufgabenstellung
Lassen wir frei gestalten.

```html
<!DOCTYPE html>
<html lang="de">
<head>
<meta charset="utf-8">
<title>Innenseiten – Broschüre hopvia</title>
<link rel="stylesheet" href="https://fonts.googleapis.com/css2?family=Raleway:wght@400;500;700&display=swap">
<style>
  :root {
    --bg: #ffffff;
    --ink: #4a4a4a;
    --title: #555555;
    --rule: #6f6f6f;
    --red: #e3222f;
    --panel: #a5aab7;
    --ghost: #e4e6eb;
    --body: #5b6070;
    --frame: #ffffff;
  }
  * { margin: 0; padding: 0; box-sizing: border-box; }
  html, body { width: 1200px; height: 707px; overflow: hidden; background: var(--bg); }
  body { position: relative; font-family: "Raleway", Arial, sans-serif; color: var(--ink); }

  .board-title {
    position: absolute; left: 0; top: 22px; width: 1200px;
    text-align: center; font-size: 38px; font-weight: 700; color: var(--title);
    letter-spacing: 0.5px;
  }
  .board-rule { position: absolute; left: 0; top: 78px; width: 1143px; height: 1px; background: var(--rule); }

  .page {
    position: absolute; background: #fff; overflow: hidden;
    box-shadow: 2px 3px 8px rgba(0,0,0,0.35);
  }
  .page--intro { left: 86px; top: 103px; width: 577px; height: 409px; z-index: 2; }
  .page--offers { left: 553px; top: 250px; width: 576px; height: 409px; z-index: 1; }

  .side-panel { position: absolute; left: 0; top: 0; width: 289px; height: 100%; background: var(--panel); }

  .photo { position: absolute; }
  .band { position: absolute; left: 0; width: 100%; }

  .ghost-heading {
    position: absolute; font-size: 21px; font-weight: 700; color: var(--ghost); white-space: nowrap;
  }
  .section-heading {
    position: absolute; font-size: 12px; font-weight: 700; color: var(--red); white-space: nowrap;
  }
  .copy { position: absolute; width: 195px; font-size: 7.4px; line-height: 9.2px; color: var(--body); }
  .copy p + p { margin-top: 9px; }

  .snapshot {
    position: absolute; background: var(--frame); padding: 4px;
    box-shadow: 1px 2px 5px rgba(0,0,0,0.35);
  }
  .snapshot div { width: 100%; height: 100%; }
</style>
</head>
<body>
  <h1 class="board-title">Innenseiten</h1>
  <div class="board-rule"></div>

  <!-- Spread: offers -->
  <section class="page page--offers">
    <div class="photo" style="left:0;top:0;width:286px;height:123px;background:linear-gradient(180deg,#7fa6d8 0%,#b9cde6 45%,#8a9a6a 70%,#3f6fa3 100%);" role="img" aria-label="Foto: Kinder springen auf einem Wasserpark-Element im See"></div>
    <div class="photo" style="left:286px;top:0;width:290px;height:123px;background:linear-gradient(135deg,#8fb0d6 0%,#5f6e62 45%,#2b2b2b 70%,#6b6b6b 100%);" role="img" aria-label="Foto: aufblasbare Fußball-Dartscheibe vor einem Gebäude"></div>
    <svg class="band" style="top:88px;height:60px" width="576" height="60" viewBox="0 0 576 60">
      <path d="M0 24 Q288 14 576 6 L576 60 L0 60 Z" fill="#ffffff"/>
      <path d="M0 24 Q288 14 576 6 L576 30 Q288 36 0 42 Z" fill="var(--red)"/>
    </svg>

    <div class="ghost-heading" style="left:30px;top:154px;">Wasserparks</div>
    <div class="section-heading" style="left:48px;top:178px;">Wasserparks - Erfrischend fröhlich</div>
    <div class="copy" style="left:56px;top:200px;">
      <p>Donec sodales sagittis magna. Morbi mollis tellus ac sapien. Curabitur suscipit suscipit tellus. Aenean commodo ligula eget dolor. Pellentesque habitant morbi tristique senectus et netus et malesuada fames ac turpis egestas.</p>
      <p>Vestibulum suscipit nulla quis orci. Integer ante arcu, accumsan a, consectetuer eget, posuere ut, mauris. Nullam cursus lacinia erat. Phasellus volutpat, metus eget egestas mollis, lacus lacus blandit dui, id egestas quam mauris ut lacus. Praesent porttitor, nulla vitae posuere iaculis, arcu nisl dignissim dolor, a pretium mi sem ut ipsum.</p>
    </div>

    <div class="ghost-heading" style="left:321px;top:154px;">Hüpfburgen</div>
    <div class="section-heading" style="left:347px;top:178px;">Hüpfburgen - Spaß für jedermann</div>
    <div class="copy" style="left:347px;top:200px;">
      <p>Donec sodales sagittis magna. Morbi mollis tellus ac sapien. Curabitur suscipit suscipit tellus. Aenean commodo ligula eget dolor. Pellentesque habitant morbi tristique senectus et netus et malesuada fames ac turpis egestas.</p>
      <p>Vestibulum suscipit nulla quis orci. Integer ante arcu, accumsan a, consectetuer eget, posuere ut, mauris. Nullam cursus lacinia erat. Phasellus volutpat, metus eget egestas mollis, lacus lacus blandit dui, id egestas quam mauris ut lacus. Praesent porttitor, nulla vitae posuere iaculis, arcu nisl dignissim dolor, a pretium mi sem ut ipsum.</p>
    </div>

    <div class="snapshot" style="left:21px;top:322px;width:120px;height:95px;transform:rotate(-3deg);">
      <div style="background:linear-gradient(160deg,#9cc0e4 0%,#f2c530 45%,#2c56a8 75%,#4f86b8 100%);" role="img" aria-label="Foto: Wasserrutsche im See"></div>
    </div>
    <div class="snapshot" style="left:148px;top:320px;width:126px;height:95px;transform:rotate(2deg);">
      <div style="background:linear-gradient(180deg,#8fb3dc 0%,#c8d8ea 40%,#e6d9a8 65%,#3d74a8 100%);" role="img" aria-label="Foto: Kinder auf einem Wasserpark-Element"></div>
    </div>
    <div class="snapshot" style="left:312px;top:334px;width:88px;height:85px;transform:rotate(-4deg);">
      <div style="background:linear-gradient(160deg,#58b5e6 0%,#f4d23a 40%,#e53b3b 70%,#3ca84a 100%);" role="img" aria-label="Foto: bunte Hüpfburg"></div>
    </div>
    <div class="snapshot" style="left:399px;top:312px;width:92px;height:105px;">
      <div style="background:radial-gradient(circle at 50% 45%,#d42a2a 0%,#f2f2f2 25%,#1d1d1d 45%,#6f7d8c 80%);" role="img" aria-label="Foto: aufblasbare Dartscheibe"></div>
    </div>
    <div class="snapshot" style="left:490px;top:326px;width:74px;height:80px;transform:rotate(4deg);">
      <div style="background:linear-gradient(160deg,#a9c7e8 0%,#e79aa6 45%,#f0c2c9 75%,#7a5fa0 100%);" role="img" aria-label="Foto: Hüpfburg in Tierform"></div>
    </div>
  </section>

  <!-- Spread: intro -->
  <section class="page page--intro">
    <div class="side-panel" role="img" aria-label="Graue Fläche mit dezentem Netzmuster"></div>
    <div class="photo" style="left:289px;top:0;width:288px;height:135px;background:linear-gradient(180deg,#6f9fd6 0%,#c9daee 35%,#6d8aa3 55%,#4a7090 65%,#5d7a4a 80%,#e8e8e8 100%);" role="img" aria-label="Foto: Stehtische mit weißen Hussen am Seeufer mit Segelbooten"></div>
    <svg class="band" style="left:289px;top:110px;width:288px;height:50px" width="288" height="50" viewBox="0 0 288 50">
      <path d="M0 14 Q144 18 288 2 L288 50 L0 50 Z" fill="#ffffff"/>
      <path d="M0 14 Q144 18 288 2 L288 22 Q144 34 0 38 Z" fill="var(--red)"/>
    </svg>

    <div class="ghost-heading" style="left:312px;top:164px;">hopvia - Das sind wir</div>
    <div class="section-heading" style="left:337px;top:188px;">hopvia - Das sind wir</div>
    <div class="copy" style="left:337px;top:211px;">
      <p>Donec sodales sagittis magna. Morbi mollis tellus ac sapien. Curabitur suscipit suscipit tellus. Aenean commodo ligula eget dolor. Pellentesque habitant morbi tristique senectus et netus et malesuada fames ac turpis egestas.</p>
      <p>Vestibulum suscipit nulla quis orci. Integer ante arcu, accumsan a, consectetuer eget, posuere ut, mauris. Nullam cursus lacinia erat. Phasellus volutpat, metus eget egestas mollis, lacus lacus blandit dui, id egestas quam mauris ut lacus. Praesent porttitor, nulla vitae posuere iaculis, arcu nisl dignissim dolor, a pretium mi sem ut ipsum.</p>
      <p>Suspendisse nisl elit, rhoncus eget, elementum ac, condimentum eget, diam. Nam at tortor in tellus interdum sagittis. In consectetuer turpis ut velit. Vestibulum dapibus nunc ac augue. Nulla porta dolor.</p>
    </div>
  </section>
</body>
</html>
```